***Design a Nutritional Supplement Label for Bright Harvest!***

I have an existing label, I want to keep the logo but change the rest of the design. I am open to different creative ideas, but it needs to look appropriate for the shelves at Bright Harvest. This means it needs to look professional and premium, without being sterile and boring. I feel like my current label looks a little 1990s. You can play with the colors, font and design elements, while keeping the logo, descriptive text and the same layout. Feel free to take some bold chances. (You cannot change the font in the supplement facts section)

Font styles to use
Sans Serif

Colors

Designer to choose colors to be used in the design.

Requirements
Must have
• Keep the same text and layout. Keep the "Muscle Haven" logo as-is. DO NOT CHANGE THE LOGO!!

```html
<!DOCTYPE html>
<html lang="en">
<head>
<meta charset="utf-8">
<title>Muscle Haven – Supplement Label</title>
<link href="https://fonts.googleapis.com/css2?family=Montserrat:wght@500;600;700&family=Roboto:wght@400;500&display=swap" rel="stylesheet">
<style>
  :root {
    --blue-deep: #1f7fae;
    --blue-mid: #3a9bc6;
    --blue-light: #6fbfe0;
    --gold: #e2b04a;
    --gold-pale: #f3d98d;
    --green: #9cc34a;
    --green-dark: #86ad35;
    --white: #ffffff;
    --paper: #eef0f2;
    --ink-blue: #5aaedb;
  }
  * { margin: 0; padding: 0; box-sizing: border-box; }
  html, body { width: 1200px; height: 1184px; overflow: hidden; background: var(--white); }
  .canvas { position: relative; width: 1200px; height: 1184px; }
  .label {
    position: absolute; left: 100px; top: 212px;
    width: 1000px; height: 760px; overflow: hidden;
    font-family: "Roboto", sans-serif;
  }
  .label-art { position: absolute; inset: 0; }
  .brand { position: absolute; left: 0; width: 920px; text-align: center; top: 200px; color: var(--ink-blue); font-family: "Montserrat", sans-serif; font-weight: 600; }
  .brand-main { display: block; font-size: 104px; line-height: 1; letter-spacing: 0.02em; }
  .brand-sub { display: block; font-size: 44px; letter-spacing: 0.55em; margin-top: 22px; padding-left: 0.55em; }
  .feature { position: absolute; color: var(--white); font-size: 34px; letter-spacing: 0.01em; }
  .feature-absorption { left: 200px; top: 450px; }
  .feature-acting { left: 200px; top: 516px; }
  .count { position: absolute; left: 90px; top: 648px; width: 120px; text-align: center; color: var(--white); font-family: "Montserrat", sans-serif; }
  .count-number { display: block; font-size: 40px; font-weight: 700; line-height: 1.05; }
  .count-unit { display: block; font-size: 19px; font-weight: 500; letter-spacing: 0.03em; }
  .divider { position: absolute; left: 222px; top: 652px; width: 2px; height: 92px; background: var(--white); opacity: 0.85; }
  .category { position: absolute; left: 248px; top: 680px; color: var(--white); font-family: "Montserrat", sans-serif; font-weight: 600; font-size: 22px; letter-spacing: 0.04em; }
</style>
</head>
<body>
<div class="canvas">
  <div class="label">
    <svg class="label-art" width="1000" height="760" viewBox="0 0 1000 760">
      <rect width="1000" height="760" fill="var(--blue-deep)"/>
      <path d="M0,110 C140,30 340,10 520,10 C760,10 940,180 960,420 L1000,420 L1000,0 L0,0 Z" fill="var(--blue-mid)"/>
      <path d="M0,150 C120,80 330,55 500,55 C720,55 870,220 870,440 C870,560 830,630 790,650 L0,650 Z" fill="var(--paper)"/>
      <path d="M0,135 C120,65 330,40 500,40 C740,40 890,210 890,440 C890,570 850,640 800,665" fill="none" stroke="var(--gold)" stroke-width="5"/>
      <path d="M0,150 C120,80 330,55 500,55 C720,55 870,220 870,440" fill="none" stroke="var(--gold-pale)" stroke-width="3"/>
      <path d="M30,210 C0,380 20,560 80,650" fill="none" stroke="var(--gold)" stroke-width="5"/>
      <!-- feature bars -->
      <polygon points="130,444 560,444 530,500 130,500" fill="var(--blue-mid)"/>
      <polygon points="130,510 500,510 470,566 130,566" fill="var(--blue-mid)"/>
      <polygon points="562,444 574,444 544,500 532,500" fill="var(--gold)"/>
      <polygon points="502,510 514,510 484,566 472,566" fill="var(--gold)"/>
      <g role="img" aria-label="Joint icon in hexagon">
        <polygon points="95,440 155,440 188,505 155,570 95,570 62,505" fill="var(--blue-mid)" stroke="var(--gold)" stroke-width="5"/>
      </g>
      <!-- bottom band -->
      <path d="M0,700 L1000,700 L1000,760 L0,760 Z" fill="var(--green)"/>
      <path d="M0,640 L760,640 C780,640 790,650 800,668 L820,700 L1000,700 L1000,760 L0,760 Z" fill="var(--green)"/>
      <path d="M0,640 L760,640 C780,640 790,650 800,668 L820,700 L1000,700" fill="none" stroke="var(--gold)" stroke-width="4"/>
      <rect x="0" y="742" width="1000" height="18" fill="var(--green-dark)"/>
    </svg>

    <div class="brand">
      <span class="brand-main">MUSCLE</span>
      <span class="brand-sub">HAVEN</span>
    </div>

    <div class="feature feature-absorption">HIGH ABSORPTION</div>
    <div class="feature feature-acting">FAST ACTING</div>

    <div class="count">
      <span class="count-number">180</span>
      <span class="count-unit">CAPSULES</span>
    </div>
    <div class="divider"></div>
    <div class="category">DIETARY SUPPLEMENT</div>
  </div>
</div>
</body>
</html>
```